I need a business card representing my company, VELDRA, it's an artist management and design company. Complete name is "VELDRA Artist Mgmt. + Design Co." I need it to be world class and very appealing, sophisticated and artistically unique.
Updates

Posted an updated Brief please see. I need a business card representing my company, VELDRA, it's an artist management and design company. Complete name is "VELDRA Artist Mgmt. + Design Co." I need it to be world class and very appealing, sophisticated and artistically unique.

Designs look the same

Designs look the same

Target Market(s)

Advertisers, Entertainment Companies, Commercial companies

Industry/Entity Type

Advertising

Contact Information for Business Card

I need a business card representing my company, VELDRA, it's an artist management and design company. Complete name is "VELDRA Artist Mgmt. + Design Co." I need it to be world class and very appealing, sophisticated and artistically unique. One side can be VELDRA Artist Mgmt. + Design Co. and the other my name, Teodoro Lindqvist, my contact telephone: 412.638.2957, email veldraartist@plumora.net, my address: 3264 Harwell Ave. #517 Miami, FL 33184

Font styles to use
Other font styles liked:
• Calibri

Colors
ffffff
0455a3
f37122

Requirements
Must have
• "VELDRA" stand out bigger than the rest of the text.
Nice to have
• Name "VELDRA" can be centered on one side or in the corner or along side edges, just need something cool and different.
Should not have
• I am open just try to keep it clean looking

```html
<!DOCTYPE html>
<html lang="en">
<head>
<meta charset="UTF-8">
<title>VELDRA Artist Mgmt. + Design Co. — Business Card</title>
<link rel="stylesheet" href="https://fonts.googleapis.com/css2?family=Carlito:wght@400;700&display=swap">
<style>
  :root {
    --stage: #2f343c;
    --white: #ffffff;
    --brand-blue: #0455a3;
    --mid-blue: #2a8ed6;
    --glow-cyan: #27c7dc;
    --text-blue: #1b86c8;
    --label-cyan: #2fb3dd;
    --orange: #f37122;
    --orange-soft: #f7a05a;
  }
  * { margin: 0; padding: 0; box-sizing: border-box; }
  html, body {
    width: 1200px; height: 1000px; overflow: hidden;
    background: var(--stage);
    font-family: "Carlito", "Calibri", sans-serif;
  }
  .card {
    position: absolute; left: 250px;
    width: 700px; height: 400px;
    overflow: hidden; background: var(--white);
    box-shadow: 0 18px 40px rgba(0,0,0,0.45);
  }
  .card-contact { top: 70px; }
  .card-brand { top: 530px; }
  .card-art { position: absolute; inset: 0; width: 700px; height: 400px; }

  /* contact side */
  .corner-logo { position: absolute; left: 26px; top: 22px; color: var(--white); }
  .corner-logo .wordmark { font-size: 54px; letter-spacing: 2px; line-height: 1; }
  .corner-logo .tagline { font-size: 11px; margin-top: 2px; }

  .person { position: absolute; right: 34px; top: 138px; text-align: right; }
  .person .name { font-size: 40px; color: var(--orange-soft); line-height: 1; }
  .person .name .surname { color: var(--text-blue); }
  .person .rule { height: 2px; background: var(--label-cyan); width: 320px; margin: 8px 0 4px auto; }
  .person .company { font-size: 11px; color: var(--text-blue); }

  .contact-list { position: absolute; right: 34px; top: 250px; text-align: right; list-style: none; font-size: 19px; line-height: 1.3; }
  .contact-list .label { color: var(--label-cyan); }
  .contact-list .value { color: var(--orange); }

  /* brand side */
  .center-logo { position: absolute; left: 150px; top: 132px; color: var(--white); }
  .center-logo .tagline { font-size: 19px; margin-bottom: 4px; }
  .center-logo .wordmark { font-size: 84px; letter-spacing: 4px; line-height: 1; }
</style>
</head>
<body>

<section class="card card-contact" aria-label="Business card, contact side">
  <svg class="card-art" viewBox="0 0 700 400" aria-hidden="true">
    <defs>
      <radialGradient id="contactGlow" cx="0.18" cy="0.35" r="0.7">
        <stop offset="0" stop-color="#27c7dc"/>
        <stop offset="0.5" stop-color="#2a8ed6"/>
        <stop offset="1" stop-color="#2a8ed6"/>
      </radialGradient>
    </defs>
    <polygon points="0,0 450,0 175,400 0,400" fill="url(#contactGlow)"/>
    <line x1="453" y1="0" x2="178" y2="400" stroke="#f7a05a" stroke-width="4"/>
  </svg>
  <div class="corner-logo">
    <div class="wordmark">VELDRA</div>
    <div class="tagline">VELDRA Artist Mgmt. + Design Co.</div>
  </div>
  <div class="person">
    <div class="name">Teodoro <span class="surname">Lindqvist</span></div>
    <div class="rule"></div>
    <div class="company">VELDRA Artist Mgmt. + Design Co.</div>
  </div>
  <ul class="contact-list">
    <li><span class="label">telephone:</span> <span class="value">412.638.2957</span></li>
    <li><span class="label">email:</span> <span class="value">veldraartist@plumora.net</span></li>
    <li><span class="label">address:</span> <span class="value">3264 Harwell Ave. #517 Miami</span></li>
    <li><span class="value">FL 33184</span></li>
  </ul>
</section>

<section class="card card-brand" aria-label="Business card, logo side">
  <svg class="card-art" viewBox="0 0 700 400" aria-hidden="true">
    <defs>
      <radialGradient id="brandGlow" cx="0.32" cy="0.3" r="0.75">
        <stop offset="0" stop-color="#27c7dc"/>
        <stop offset="0.45" stop-color="#2a8ed6"/>
        <stop offset="1" stop-color="#1a62ad"/>
      </radialGradient>
    </defs>
    <polygon points="0,0 620,0 500,400 0,400" fill="url(#brandGlow)"/>
    <line x1="640" y1="0" x2="520" y2="400" stroke="#0455a3" stroke-width="4"/>
    <line x1="650" y1="0" x2="530" y2="400" stroke="#f37122" stroke-width="4"/>
  </svg>
  <div class="center-logo">
    <div class="tagline">VELDRA Artist Mgmt. + Design Co.</div>
    <div class="wordmark">VELDRA</div>
  </div>
</section>

</body>
</html>
```